QuoteMarlin.com Homepage Redesign

Create a new homepage design for our website QuoteMarlin.com. Our current experience is focused on auto insurance only. We would like to incorporate the ability to receive rate estimates for home insurance and bundled (home + auto) insurance in addition to auto. Home insurance will include home, renters and condo. The final design should inspire users to utilize our comparison tool.

Industry/Entity Type

Insurance (Auto & Home)

Number of Pages Required

1 page

Font styles to use
Other font styles liked:
• See Assets - Sans Serif & Roboto

Colors
0054AA
0677BA
7BADD7
CADEEF
E8F1F8
59FF00
82FF00
B8FF75
E3FFCB
F4FFEA

Requirements
Must have
• Must include the ability to launch our rate comparison tool within the main hero image for Auto, Home, Bundled.
Nice to have
• The design should be bold and eye catching. It should be differentiated from the typical landing page experience. (Some of our favorite sites from a UX perspective include: Vaultline.org, ThePelican.com, Ferrow.com and Corvane Airways - They are busy but we like the app like approach on the homepage)
Should not have
• We are not looking for a design that is heavy on generic images.

```html
<!DOCTYPE html>
<html lang="en">
<head>
<meta charset="utf-8">
<title>QuoteMarlin – Compare Home &amp; Auto Insurance</title>
<link href="https://fonts.googleapis.com/css2?family=Red+Hat+Display:wght@400;500;600;700;800&display=swap" rel="stylesheet">
<style>
:root{
  --blue:#1a5cf5;
  --blue-deep:#0054aa;
  --blue-soft:#cadeef;
  --blue-mist:#eef4fc;
  --green:#3fe03a;
  --green-bright:#59ff00;
  --green-lime:#82ff00;
  --ink:#111418;
  --muted:#5f6670;
  --line:#d9e2ee;
  --red:#e2262b;
  --white:#fff;
}
*{box-sizing:border-box;margin:0;padding:0}
html,body{width:1200px;height:3892px;overflow:hidden}
body{position:relative;font-family:"Red Hat Display",sans-serif;color:var(--ink);background:var(--white)}
.abs{position:absolute}
.btn{position:absolute;display:flex;align-items:center;justify-content:center;gap:10px;border-radius:30px;background:var(--blue);color:#fff;font-weight:600;font-size:13px}
.btn svg{position:absolute;left:30px}

/* hero */
.hero-bg{left:0;top:0;width:1200px;height:720px;background:linear-gradient(180deg,#f2f6ff 0%,#f6f9ff 70%,#fff 100%)}
.brand{left:103px;top:26px;display:flex;align-items:center;gap:8px;font-weight:700;font-size:24px;color:var(--blue-deep)}
.brand i{width:22px;height:22px;border-radius:50%;background:var(--blue);display:block}
.nav-tab{left:452px;top:0;width:97px;height:65px;background:#dfe9fb;border-radius:0 0 6px 6px}
.nav a{position:absolute;top:32px;font-size:14px;color:var(--ink);text-decoration:none}
.hero-title{left:0;width:1200px;top:138px;text-align:center;font-size:42px;font-weight:700}
.hero-title span{color:var(--blue)}
.hero-sub{left:0;width:1200px;top:201px;text-align:center;font-size:19px;font-weight:500}
.form-card{left:166px;top:254px;width:869px;height:402px;background:#fff;border-radius:14px;box-shadow:0 8px 40px rgba(40,80,160,.10)}
.step-line{left:290px;top:305px;width:556px;border-top:1px dashed #c5cfdd}
.step{position:absolute;width:44px;height:44px;border-radius:50%;background:#e5e9ef;display:flex;align-items:center;justify-content:center;top:283px}
.step.active{width:58px;height:58px;top:276px;background:var(--blue)}
.step-label{position:absolute;top:348px;font-size:15px;width:260px;text-align:center}
.field{position:absolute;height:38px;border:1px solid var(--line);border-radius:8px;background:#f9fbfd;font-size:15px;color:#9aa3ae;display:flex;align-items:center;padding:0 26px}
.field .caret{position:absolute;right:28px;top:15px;border:5px solid transparent;border-top:6px solid #222}
.toggle{left:650px;top:564px;width:317px;height:36px;border:1px solid var(--line);border-radius:8px;background:#f9fbfd}
.toggle span{position:absolute;top:0;height:34px;width:156px;display:flex;align-items:center;justify-content:center;font-size:16px}
.results{left:559px;top:635px;width:413px;height:43px;background:var(--green);color:#fff;font-size:18px;font-weight:600;border-radius:8px;display:flex;align-items:center;justify-content:center}
.partners{left:254px;top:758px;width:728px;display:flex;justify-content:space-between;align-items:center}
.partners i{display:block;height:16px;width:72px;background:#c7ccd4;border-radius:3px}

/* about */
.photo{border-radius:10px}
.eyebrow{font-size:15px;font-weight:600;color:var(--blue)}
.about-title{font-size:27px;font-weight:400;letter-spacing:.5px}
.about-title b{font-weight:700}
.body-text{font-size:13.5px;line-height:22px;color:var(--muted)}
.tab{position:absolute;left:600px;width:319px;height:72px;border-radius:6px;display:flex;align-items:center;padding-left:86px;font-size:19px;font-weight:600}
.tab svg{position:absolute;left:22px}
.tab.active{background:var(--blue);color:#fff}

/* tacoma compare */
.compare-bg{left:0;top:1605px;width:1200px;height:604px;background:linear-gradient(180deg,#eef5ff,#f4f8ff)}
.green-title{font-size:34px;font-weight:800;color:var(--green)}
.col-title{font-size:26px;font-weight:700;line-height:24px}
.col-title small{display:block;font-size:20px;font-weight:400}
.col-title small b{font-weight:600}

/* consult band */
.band{left:0;top:2209px;width:1200px;height:375px;background:linear-gradient(100deg,var(--green-lime),#3de01a 60%,#42d83a)}
.band-center{left:0;width:1200px;text-align:center;color:#fff}

/* testimonials */
.t-card{position:absolute;background:#fff;border-radius:6px;box-shadow:0 6px 30px rgba(0,0,0,.08);padding:36px 34px}
.t-card h3{font-size:25px;font-weight:600}
.t-card h3 span{font-weight:400}
.stars{color:#f5c400;font-size:18px;letter-spacing:2px;margin:18px 0 8px}
.t-card p{font-size:13px;line-height:22px;color:var(--muted)}
.avatar{border-radius:50%;background:linear-gradient(135deg,#c8e85a,#e8b0c8)}

/* footer */
.footer-bg{left:0;top:3581px;width:1200px;height:311px;background:#f6f9ff}
.f-title{font-size:25px;font-weight:700}
.f-title span{font-weight:400}
.f-links{list-style:none;font-size:13px;font-weight:500}
.f-links li{height:26px;display:flex;align-items:center;gap:12px}
.social i{display:inline-block;width:15px;height:15px;border-radius:50%;background:var(--ink);margin-right:14px}
</style>
</head>
<body>

<!-- HERO -->
<div class="abs hero-bg"></div>
<div class="abs brand"><i></i>QuoteMarlin</div>
<div class="abs nav-tab"></div>
<nav class="nav">
  <a style="left:482px;color:var(--blue)">Home</a>
  <a style="left:591px">Services</a>
  <a style="left:718px">Contact</a>
</nav>
<div class="btn" style="left:943px;top:15px;width:171px;height:44px;border-radius:8px;font-size:14px;padding-left:30px">
  <svg width="14" height="14" viewBox="0 0 24 24" fill="#fff" style="left:18px"><path d="M6.6 10.8a15 15 0 006.6 6.6l2.2-2.2a1 1 0 011-.25 11 11 0 003.6.6 1 1 0 011 1V20a1 1 0 01-1 1A17 17 0 013 4a1 1 0 011-1h3.5a1 1 0 011 1c0 1.25.2 2.45.6 3.6a1 1 0 01-.25 1z"/></svg>Call Now</div>

<svg class="abs" style="left:268px;top:112px" width="120" height="140" viewBox="0 0 120 140" fill="none" stroke="var(--green)" stroke-width="2" stroke-dasharray="5 5"><path d="M118 30C90 0 30 -5 10 40 0 70 12 100 14 130"/><path d="M8 120l6 12 6-12" stroke-dasharray="none"/></svg>
<h1 class="abs hero-title"><span>Home Insurance</span> get started</h1>
<p class="abs hero-sub">Personalized results in 30 seconds. No email or phone required</p>

<div class="abs form-card"></div>
<div class="abs step-line"></div>
<div class="step active" style="left:261px"><svg width="26" height="26" viewBox="0 0 24 24" fill="none" stroke="#fff" stroke-width="1.8"><path d="M3 11l9-7 9 7v9h-6v-6H9v6H3z"/></svg></div>
<div class="step" style="left:546px"><svg width="20" height="20" viewBox="0 0 24 24" fill="#8a93a0"><path d="M5 11l2-5h10l2 5v7h-2v-2H7v2H5z"/></svg></div>
<div class="step" style="left:824px"><svg width="20" height="20" viewBox="0 0 24 24" fill="none" stroke="#8a93a0" stroke-width="1.8"><path d="M4 12l8-7 8 7v8H4z"/></svg></div>
<div class="step-label" style="left:168px;color:var(--blue)">Home Isurance</div>
<div class="step-label" style="left:442px">Automobile Insurance</div>
<div class="step-label" style="left:719px">Home &amp; Automobile Insurance</div>

<div class="field" style="left:234px;top:391px;width:732px">Current Provider<i class="caret"></i></div>
<svg class="abs" style="left:209px;top:459px" width="18" height="18" viewBox="0 0 18 18" fill="none" stroke="#444"><circle cx="9" cy="9" r="7.5"/><path d="M9 8v5M9 5.5v.5"/></svg>
<div class="field" style="left:234px;top:449px;width:732px">Credit Score<i class="caret"></i></div>
<div class="field" style="left:234px;top:506px;width:384px">Zip code</div>
<div class="field" style="left:650px;top:506px;width:314px">How old are you?</div>
<div class="abs" style="left:400px;width:215px;top:571px;text-align:right;font-size:16px">Do you own a house?</div>
<div class="abs toggle">
  <span style="left:0;color:#9aa3ae">No</span>
  <span style="left:160px;background:var(--blue);color:#fff;border-radius:7px;font-weight:600">Yes</span>
</div>
<div class="abs results">Results</div>

<div class="abs partners" aria-label="Partner insurers">
  <i></i><i></i><i></i><i></i><i></i><i></i><i></i><i style="width:56px;height:28px"></i>
</div>

<!-- ABOUT -->
<div class="abs photo" role="img" aria-label="Blue two-storey house with a green lawn and trees" style="left:106px;top:922px;width:443px;height:610px;background:linear-gradient(180deg,#e8f2fb 0%,#9cbf8a 30%,#2e5f9a 50%,#3a6aa8 65%,#5f9a3a 80%,#7db048 100%)"></div>
<div class="abs eyebrow" style="left:600px;top:962px">ABOUT</div>
<h2 class="abs about-title" style="left:600px;top:982px"><b>HOME</b> INSURANCE</h2>
<p class="abs body-text" style="left:600px;top:1057px;width:480px">Lorem ipsum dolor sit amet, consectetur adipiscing elit. Nunc sed lorem ac elit consequat tristique. Quisque commodo, magna sit amet commodo hendrerit, ligula arcu tristique lacus, sit amet tincidunt justo felis in mauris.</p>
<div class="tab active" style="top:1189px">
  <svg width="40" height="48" viewBox="0 0 40 48" fill="none" stroke="#fff" stroke-width="1.6"><circle cx="20" cy="18" r="13"/><circle cx="20" cy="18" r="7"/><path d="M12 29l-4 15 6-4 4 6 2-14M28 29l4 15-6-4-4 6"/></svg>Home</div>
<div class="tab" style="top:1280px">
  <svg width="50" height="40" viewBox="0 0 50 40" fill="none" stroke="#333" stroke-width="1.5"><rect x="4" y="3" width="42" height="22" rx="3"/><circle cx="12" cy="29" r="4"/><circle cx="25" cy="29" r="4"/><circle cx="38" cy="29" r="4"/></svg>Automotive</div>
<div class="tab" style="top:1371px">
  <svg width="50" height="46" viewBox="0 0 50 46" fill="none" stroke="#333" stroke-width="1.5"><rect x="18" y="3" width="8" height="24" rx="3"/><path d="M22 27v6M10 40h30M14 40c0-8 8-12 16-8"/></svg>Home and automotive</div>
<svg class="abs" style="left:606px;top:1492px" width="130" height="4"><rect width="14" height="4" rx="2" fill="#bbb"/><rect x="26" width="50" height="4" rx="2" fill="var(--green)"/><rect x="88" width="14" height="4" rx="2" fill="#bbb"/><rect x="114" width="14" height="4" rx="2" fill="#bbb"/></svg>

<!-- COMPARE -->
<div class="abs compare-bg"></div>
<div class="abs green-title" style="left:115px;top:1658px">TACOMA?</div>
<svg class="abs" style="left:121px;top:1720px" width="400" height="26"><rect x="0" y="11" width="152" height="4" fill="var(--green)"/><rect x="156" y="11" width="84" height="4" fill="var(--blue)"/><rect x="244" y="11" width="150" height="4" fill="var(--red)"/><circle cx="76" cy="13" r="11" fill="#fff" stroke="var(--green)" stroke-width="3"/></svg>
<div class="abs" style="left:113px;top:1756px;font-size:25px;font-weight:600;color:#8ab8ea">Find the Best Insurance Offers</div>
<p class="abs body-text" style="left:115px;top:1804px;width:425px">Suspendisse vel orci faucibus, porta mauris at, suscipit lectus. Nulla nec dapibus quam. Mauris eu urna sed est facilisis iaculis. Curabitur egestas mollis odio in ullamcorper. Aenean dignissim facilisis ligula, id eleifend ante tincidunt ac. Sed congue eget risus sit amet dignissim. Yullamcorper nulla convallis eu. Nullam id velit dui.</p>
<div class="abs col-title" style="left:117px;top:1982px">SUSPENDISSE<small><b>Suspen</b>disse</small></div>
<p class="abs body-text" style="left:117px;top:2040px;width:190px;font-size:12px">Suspendisse vel orci faucibus, porta mauris at, suscipit lectus. Nulla nec dapibus quam. Mauris eu urna sed.</p>
<div class="abs col-title" style="left:339px;top:1982px">SUSPENDISSE<small><b>Suspen</b>disse</small></div>
<p class="abs body-text" style="left:340px;top:2040px;width:190px;font-size:12px">Suspendisse vel orci faucibus, porta mauris at, suscipit lectus. Nulla nec dapibus quam. Mauris eu urna sed.</p>
<div class="abs" role="img" aria-label="Hand holding a phone showing insurance recommendations" style="left:720px;top:1655px;width:460px;height:520px;border-radius:40px 40px 120px 40px;background:linear-gradient(160deg,#e9c7b0 0%,#1b1d22 25%,#f4f7fb 40%,#eef2f8 75%,#e6bfa6 100%)"></div>

<!-- CONSULT BAND -->
<div class="abs band"></div>
<div class="abs band-center" style="top:2264px;font-size:17px;font-weight:700">NO OBLIGATIONS CONSULTING</div>
<div class="abs band-center" style="top:2284px;font-size:45px;font-weight:700;color:var(--ink)">+(1) 5550 18 204 77</div>
<div class="abs band-center" style="top:2346px;font-size:13px;line-height:23px;left:440px;width:320px">Suspendisse vel orci faucibus, porta mauris at, suscipit lectus. Nulla nec dapibus quam.</div>
<div class="btn" style="left:408px;top:2425px;width:384px;height:38px">
  <svg width="14" height="14" viewBox="0 0 24 24" fill="#fff"><path d="M6.6 10.8a15 15 0 006.6 6.6l2.2-2.2a1 1 0 011-.25 11 11 0 003.6.6 1 1 0 011 1V20a1 1 0 01-1 1A17 17 0 013 4a1 1 0 011-1h3.5a1 1 0 011 1c0 1.25.2 2.45.6 3.6a1 1 0 01-.25 1z"/></svg>Call Now</div>

<!-- TESTIMONIALS -->
<div class="t-card" style="left:-20px;top:2516px;width:174px;height:288px;padding:140px 0 0 20px"><p>Mauris eu urna sed sis ligula, id eleif-<br><br><br>uis porttitor porta.</p></div>
<div class="t-card" style="left:237px;top:2520px;width:733px;height:287px">
  <h3>Living Life like <span>Never!</span></h3>
  <div class="stars">★★★★★</div>
  <p>Suspendisse vel orci faucibus, porta mauris at, suscipit lectus. Nulla nec dapibus quam. Mauris eu urna sed est facilisis iaculis. Curabitur egestas mollis odio in ullamcorper. Aenean dignissim facilisis ligula, id eleifend ante tincidunt ac. Sed congue eget risus sit amet dignissim.</p>
  <p style="margin-top:20px">Mauris pulvinar risus in sem malesuada, id sagittis est scelerisque. Morbi congue erat quis porttitor porta. In posuere vehicula ante, in ullamcorper nulla convallis eu. Nullam id velit dui.</p>
</div>
<svg class="abs" style="left:295px;top:2805px" width="36" height="18"><path d="M0 0h36L18 18z" fill="#fff"/></svg>
<div class="t-card" style="left:1070px;top:2516px;width:200px;height:288px;padding:36px 0 0 40px"><h3>Living Li</h3><div class="stars">★★★★★</div><p>Suspendisse vel est facilisis iacul end ante tincidu<br><br>Mauris pulvinar In posuere vehic</p></div>
<svg class="abs" style="left:183px;top:2662px" width="24" height="20" fill="none" stroke="#222" stroke-width="2"><path d="M23 10H2M10 2L2 10l8 8"/></svg>
<svg class="abs" style="left:1008px;top:2662px" width="24" height="20" fill="none" stroke="#222" stroke-width="2"><path d="M1 10h21M14 2l8 8-8 8"/></svg>
<div class="abs avatar" role="img" aria-label="Customer portrait" style="left:288px;top:2840px;width:52px;height:52px"></div>
<div class="abs" style="left:363px;top:2852px;font-size:13px;font-weight:700">NORA V.<div style="font-size:11px;font-weight:500;font-style:italic;color:#999">CEO AT LUMARO</div></div>
<div class="abs avatar" role="img" aria-label="Customer portrait" style="left:1100px;top:2840px;width:52px;height:52px"></div>
<div class="abs" style="left:1174px;top:2852px;font-size:13px;font-weight:700">NOR<div style="font-size:11px;font-weight:500;font-style:italic;color:#999">CEO</div></div>

<!-- LOCATION -->
<div class="abs photo" role="img" aria-label="Person on a rock under green northern lights above clouds" style="left:106px;top:2993px;width:393px;height:500px;background:linear-gradient(180deg,#0c1a3a 0%,#1e5a6a 30%,#4aa88a 45%,#6a98c8 70%,#f0d8c8 90%,#c8b8c8 100%)"></div>
<div class="abs green-title" style="left:606px;top:3072px">TACOMA</div>
<div class="abs" style="left:606px;top:3108px;font-size:27px;font-weight:600">Washington, <span style="font-weight:400">USA</span></div>
<p class="abs body-text" style="left:604px;top:3185px;width:430px">Suspendisse vel orci faucibus, porta mauris at, suscipit lectus. Nulla nec dapibus quam. Mauris eu urna sed est facilisis iaculis. Curabitur egestas mollis odio in ullamcorper. Aenean dignissim facilisis ligula, id eleifend ante tincidunt ac. Sed congue eget risus sit amet dignissim. Yullamcorper nulla convallis eu. Nullam id velit dui.</p>
<div class="btn" style="left:598px;top:3332px;width:384px;height:38px">Call Now</div>

<!-- FOOTER -->
<div class="abs footer-bg"></div>
<div class="abs" style="left:86px;top:3651px;width:51px;height:51px;border-radius:50%;background:var(--ink)"></div>
<div class="abs" style="left:151px;top:3662px;font-size:26px;font-weight:500">LOGO<span style="font-weight:400">THIS</span></div>
<p class="abs" style="left:85px;top:3724px;width:260px;font-size:12.5px;line-height:20px">Suspendisse vel orci faucibus, porta mauris at, suscipit lectus. Nulla nec dapibus quam.</p>
<div class="abs social" style="left:86px;top:3780px" aria-label="Social channels"><i></i><i></i><i></i><i></i><i></i></div>

<div class="abs f-title" style="left:447px;top:3644px">SUSPEN<span>DISSE</span></div>
<ul class="abs f-links" style="left:449px;top:3692px">
  <li>→ Home</li><li>→ About Us</li><li>→ Services</li><li>→ Values</li><li>→ Contact</li>
</ul>

<div class="abs f-title" style="left:795px;top:3644px">SUSPEN<span>DISSE</span></div>
<svg class="abs" style="left:795px;top:3697px" width="14" height="18" viewBox="0 0 14 18" fill="var(--ink)"><path d="M7 0a7 7 0 017 7c0 5-7 11-7 11S0 12 0 7a7 7 0 017-7zm0 4a3 3 0 100 6 3 3 0 000-6z"/></svg>
<p class="abs" style="left:820px;top:3696px;font-size:12.5px;line-height:20px;width:230px">Suspendisse vel orci faucibus, 2150 Harbor Lane, Brightwater</p>
<svg class="abs" style="left:793px;top:3754px" width="16" height="16" viewBox="0 0 24 24" fill="none" stroke="var(--ink)" stroke-width="2"><path d="M6.6 10.8a15 15 0 006.6 6.6l2.2-2.2 4.6 1.6V20A17 17 0 013 4h3.6l1.4 4.6z"/></svg>
<div class="abs" style="left:821px;top:3754px;font-size:12.5px">+1 555 010 482 19</div>
<div class="btn" style="left:772px;top:3788px;width:293px;height:37px">
  <svg width="14" height="14" viewBox="0 0 24 24" fill="#fff"><path d="M6.6 10.8a15 15 0 006.6 6.6l2.2-2.2a1 1 0 011-.25 11 11 0 003.6.6 1 1 0 011 1V20a1 1 0 01-1 1A17 17 0 013 4a1 1 0 011-1h3.5a1 1 0 011 1c0 1.25.2 2.45.6 3.6a1 1 0 01-.25 1z"/></svg>Call Now</div>
<div class="abs" style="left:86px;top:3872px;font-size:8px;color:#888">Copyright © 2023 QuoteMarlin. Use of this site means you accept our User Agreement and Privacy Policy.</div>

</body>
</html>
```